Thornwell Building Company - advertisement poster

I am looking to print some canvas signs to advertise my general contracting company, Thornwell Building Company. The sign will measure 6' long x 3' high so the size should match that ratio. I already have a logo icon, which is the Letter 'A' and some trees that I would like to incorporate, see attached. I would also like the to have the following information listed:
1) phone number: 472-318-6095
2) email: thornwellbuildingcompany@mailvistra.net
3) website: thornwellbuildingcompany.com
4) Lic#5386204
5) I want to use this text: "BUILD WITH THE T-CREW!"

The ad should be relatively simple and clean. Black and Green are my company colors. I am open to creative ideas!

Target Market(s)

People looking to renovate their homes

Industry/Entity Type

Construction

Colors
59FF00
82FF00
B8FF75
E3FFCB
F4FFEA

Requirements
Must have
• Must have my company logo
Should not have
• No photos or complex graphics

```html
<!DOCTYPE html>
<html lang="en">
<head>
<meta charset="utf-8">
<title>Thornwell Building Company – Sign</title>
<link rel="stylesheet" href="https://fonts.googleapis.com/css2?family=Arimo:wght@700&family=Oswald:wght@500&display=swap">
<style>
  :root {
    --backdrop: #9a9a9a;
    --leaf: #74b64f;
    --navy: #373568;
    --paper: #ffffff;
  }
  * { margin: 0; padding: 0; box-sizing: border-box; }
  html, body {
    width: 1200px; height: 657px; overflow: hidden;
    background: var(--backdrop);
  }
  .sign {
    position: absolute; left: 0; top: 28px;
    width: 1200px; height: 600px;
    background: var(--leaf);
    overflow: hidden;
  }
  .sign-shapes { position: absolute; inset: 0; }
  .headline {
    position: absolute; left: 823px; transform: translateX(-50%);
    font-family: "Arimo", Arial, sans-serif; font-weight: 700;
    color: var(--paper); text-align: center; white-space: nowrap;
    line-height: 1;
  }
  .headline-lead { top: 38px; font-size: 64px; }
  .headline-main { top: 96px; font-size: 126px; letter-spacing: -1px; }
  .contact {
    position: absolute; left: 610px;
    display: flex; align-items: center; gap: 26px;
    font-family: "Oswald", "Arial Narrow", sans-serif; font-weight: 500;
    color: var(--paper); white-space: nowrap; line-height: 1;
  }
  .contact svg { width: 32px; height: 32px; flex: none; }
  .contact-phone { top: 258px; font-size: 56px; }
  .contact-email { top: 355px; font-size: 31px; }
  .contact-web { top: 433px; font-size: 31px; }
  .license {
    position: absolute; left: 899px; top: 529px; transform: translateX(-50%);
    font-family: "Arimo", Arial, sans-serif; font-weight: 700;
    font-size: 36px; color: var(--paper); line-height: 1; white-space: nowrap;
  }
  .brand {
    position: absolute; left: 267px; top: 290px; transform: translateX(-50%);
    font-family: "Arimo", Arial, sans-serif; font-weight: 700;
    color: var(--navy); text-align: center; line-height: 1.1; white-space: nowrap;
  }
  .brand-name { font-size: 44px; letter-spacing: 1px; }
  .brand-sub { font-size: 19px; letter-spacing: 4px; }
</style>
</head>
<body>
  <main class="sign">
    <svg class="sign-shapes" viewBox="0 0 1200 600" aria-hidden="true">
      <polygon fill="var(--paper)" points="199,0 341,0 513,222 429,222 563,392 473,392 637,600 0,600 0,477 67,392 0,392 0,359 109,222 27,222"/>
      <polygon fill="var(--navy)" points="410,21 1200,21 1200,222 565,222"/>
      <polygon fill="var(--navy)" points="601,509 1200,509 1200,584 660,584"/>
    </svg>

    <div class="brand">
      <div class="brand-name">THORNWELL</div>
      <div class="brand-sub">BUILDING COMPANY</div>
    </div>

    <h1 class="headline headline-lead">BUILD WITH THE</h1>
    <p class="headline headline-main">T-CREW!</p>

    <div class="contact contact-phone">
      <svg viewBox="0 0 32 32" aria-hidden="true">
        <path fill="var(--navy)" d="M7 3c1-.6 2-.3 2.6.6l3 4.6c.5.8.3 1.8-.4 2.4l-2 1.6c1.2 3 3.7 5.7 6.8 7.2l1.7-1.9c.6-.7 1.7-.8 2.4-.3l4.5 3.1c.9.6 1.1 1.7.5 2.6l-1.6 2.4c-1 1.5-3 2.1-4.7 1.4C12 25 6 19 3.3 11.3c-.6-1.7 0-3.6 1.5-4.6z"/>
        <path fill="none" stroke="var(--navy)" stroke-width="2" stroke-linecap="round" d="M18 9a6 6 0 0 1 5 5M18 4a11 11 0 0 1 10 10"/>
      </svg>
      <span>472-318-6095</span>
    </div>

    <div class="contact contact-email">
      <svg viewBox="0 0 32 32" aria-hidden="true">
        <rect x="1" y="6" width="30" height="21" fill="var(--navy)"/>
        <path fill="none" stroke="var(--leaf)" stroke-width="2" d="M2 7l14 11L30 7M2 26l10-9M30 26l-10-9"/>
      </svg>
      <span>thornwellbuildingcompany@mailvistra.net</span>
    </div>

    <div class="contact contact-web">
      <svg viewBox="0 0 32 32" aria-hidden="true">
        <g fill="none" stroke="var(--navy)" stroke-width="2.4">
          <circle cx="14" cy="14" r="12"/>
          <ellipse cx="14" cy="14" rx="5" ry="12"/>
          <path d="M2 14h24M4 8h20M4 20h14"/>
        </g>
        <path fill="var(--navy)" stroke="var(--leaf)" stroke-width="1" d="M18 17l11 4-4 1.5 4 5-2 1.5-4-5-2 3.5z"/>
      </svg>
      <span>thornwellbuildingcompany.com</span>
    </div>

    <div class="license">Lic#5386204</div>
  </main>
</body>
</html>
```